Morvik Construction Business Card

I need a business card design for my company.
We are a construction/machinery company.
I would like to see my logo on the front of the card and my details on the other side
I would like the card to be black or dark grey in colour,with my logo as i send it or modified with a lighter blue colour
I would like to see the design kept fairly simple,but eye catching at the same time
Industry/Entity Type
Business
Colors
00a990
1b1b1b
000000
474747
ececec

```html
<!DOCTYPE html>
<html lang="en">
<head>
<meta charset="utf-8">
<title>Morvik Construction Business Card</title>
<link href="https://fonts.googleapis.com/css2?family=Open+Sans:wght@400;600;700&display=swap" rel="stylesheet">
<style>
  :root {
    --teal: #00a990;
    --ink: #1b1b1b;
    --black: #000000;
    --grey: #474747;
    --light: #ececec;
    --white: #ffffff;
  }
  html, body {
    margin: 0;
    width: 1200px;
    height: 913px;
    overflow: hidden;
    background: var(--light);
    font-family: "Open Sans", Arial, sans-serif;
  }
  .stage {
    position: relative;
    width: 1200px;
    height: 913px;
  }
  .card {
    position: absolute;
    width: 520px;
    height: 297px;
    border-radius: 16px;
    overflow: hidden;
    box-shadow: 0 6px 18px rgba(0,0,0,0.18);
  }
  /* Front card */
  .card-front {
    left: 90px;
    top: 150px;
    background: var(--white);
  }
  .card-front .swoosh {
    position: absolute;
    left: 0;
    top: 0;
    width: 520px;
    height: 297px;
  }
  .brand {
    position: absolute;
    left: 34px;
    top: 90px;
    width: 210px;
    display: flex;
    align-items: center;
    gap: 10px;
  }
  .brand-mark {
    width: 16px;
    height: 16px;
    background: var(--ink);
    flex: none;
  }
  .brand-name {
    font-weight: 700;
    font-size: 22px;
    line-height: 1.1;
    color: var(--ink);
    letter-spacing: 0.5px;
  }
  .divider {
    position: absolute;
    left: 262px;
    top: 62px;
    width: 1px;
    height: 100px;
    background: #bdbdbd;
  }
  .details {
    position: absolute;
    left: 278px;
    top: 56px;
  }
  .person-name {
    margin: 0;
    font-size: 20px;
    font-weight: 700;
    color: var(--grey);
  }
  .person-role {
    margin: 0 0 10px;
    font-size: 13px;
    color: var(--teal);
  }
  .contact {
    list-style: none;
    margin: 0;
    padding: 0;
    font-size: 12.5px;
    color: var(--ink);
  }
  .contact li {
    display: flex;
    align-items: center;
    gap: 7px;
    margin-bottom: 3px;
  }
  .contact svg {
    width: 11px;
    height: 11px;
    fill: var(--teal);
    flex: none;
  }
  /* Back card */
  .card-back {
    left: 590px;
    top: 440px;
    background: linear-gradient(160deg, #2a2a2a 0%, var(--black) 45%, var(--ink) 100%);
    display: flex;
    align-items: center;
    justify-content: center;
    gap: 14px;
  }
  .card-back .brand-mark {
    width: 22px;
    height: 22px;
    background: var(--white);
  }
  .card-back .brand-name {
    color: var(--white);
    font-size: 32px;
  }
</style>
</head>
<body>
<main class="stage">
  <section class="card card-front">
    <svg class="swoosh" viewBox="0 0 520 297" aria-hidden="true">
      <path d="M0 297 L0 292 Q260 268 520 202 L520 297 Z" fill="var(--teal)"/>
      <path d="M0 290 Q260 264 520 198" fill="none" stroke="var(--black)" stroke-width="3"/>
    </svg>
    <div class="brand">
      <span class="brand-mark"></span>
      <span class="brand-name">Morvik Construction</span>
    </div>
    <div class="divider"></div>
    <div class="details">
      <p class="person-name">Lena Barros</p>
      <p class="person-role">Director</p>
      <ul class="contact">
        <li>
          <svg viewBox="0 0 24 24"><path d="M6.6 10.8a15.1 15.1 0 0 0 6.6 6.6l2.2-2.2c.3-.3.7-.4 1-.2 1.1.4 2.3.6 3.6.6.6 0 1 .4 1 1V20c0 .6-.4 1-1 1A17 17 0 0 1 3 4c0-.6.4-1 1-1h3.5c.6 0 1 .4 1 1 0 1.3.2 2.5.6 3.6.1.3 0 .7-.2 1z"/></svg>
          +33 2481-5037
        </li>
        <li>
          <svg viewBox="0 0 24 24"><path d="M2 5h20v14H2z M4 7v.5l8 5 8-5V7z" fill-rule="evenodd"/></svg>
          lena@barrosmail.com
        </li>
        <li>
          <svg viewBox="0 0 24 24"><path d="M12 2a7 7 0 0 0-7 7c0 5 7 13 7 13s7-8 7-13a7 7 0 0 0-7-7zm0 9.5A2.5 2.5 0 1 1 12 6.5a2.5 2.5 0 0 1 0 5z"/></svg>
          48 Ardent Street Corlow VIC 3290
        </li>
      </ul>
    </div>
  </section>

  <section class="card card-back">
    <span class="brand-mark"></span>
    <span class="brand-name">Morvik Construction</span>
  </section>
</main>
</body>
</html>
```